Dental promotion

We are a family dental office that provides 99% of the dental service for the entire family, including IV sedation, wisdom teeth extraction, implant, Clearvanta, root canal, teeth whiting et cl. We currently have promotion for Clearvanta, implant and new patients who don’t have insurance. 1500 off Clearvanta, 2000 off for implant, 98 dollars for new patient that cover exam, x-ray, and regular cleaning. We also offer financing option.
More information please check our website
https://www.brookhollowfamilydentistry.example/

```html
<!DOCTYPE html>
<html lang="en">
<head>
<meta charset="utf-8">
<title>Brookhollow Family Dentistry – Postcard</title>
<link href="https://fonts.googleapis.com/css2?family=Anton&family=Poppins:wght@400;500;600;700&display=swap" rel="stylesheet">
<style>
  :root{
    --blue:#3a37b8;
    --blue-dark:#2b2896;
    --green:#5c9e1e;
    --ink:#111111;
    --paper:#ffffff;
    --stage:#f2f2f2;
    --stamp:#e3e3e3;
    --rule:#c8c8c8;
  }
  *{margin:0;padding:0;box-sizing:border-box}
  html,body{width:1200px;height:2467px;overflow:hidden;background:var(--stage);font-family:'Poppins',sans-serif}
  .canvas{position:relative;width:1200px;height:2467px}
  .card{position:absolute;left:81px;width:944px;height:630px;background:var(--paper);overflow:hidden;transform:scale(1.1);transform-origin:top left;box-shadow:0 6px 22px rgba(0,0,0,.18)}
  .card--front{top:490px}
  .card--back{top:1283px}
  .layer{position:absolute;inset:0}
  .brand{position:absolute;display:flex;align-items:center;gap:10px}
  .brand__dot{width:58px;height:58px;border-radius:50%;border:3px solid var(--blue);flex:none}
  .brand__name{font-size:21px;font-weight:500;color:var(--blue);line-height:1.05;letter-spacing:1px;white-space:nowrap}
  .headline{position:absolute;left:50px;top:128px;font-family:'Anton',sans-serif;color:var(--blue);font-size:64px;line-height:1;letter-spacing:-.5px;white-space:nowrap}
  .subhead{position:absolute;left:50px;top:200px;font-family:'Anton',sans-serif;color:var(--ink);font-size:50px;line-height:1;white-space:nowrap}
  .intro{position:absolute;left:50px;top:266px;width:345px;font-size:11.5px;line-height:1.38;color:var(--ink)}
  .accepting{position:absolute;left:52px;top:458px;color:#fff;font-size:26px;line-height:1.08;font-weight:400;letter-spacing:.5px;white-space:nowrap}
  .accepting strong{display:block;font-weight:700;font-size:36px}
  .accepting__rule{position:absolute;left:52px;top:596px;width:68px;height:4px;background:var(--blue)}
  .contact-title{position:absolute;left:459px;top:530px;font-size:25px;font-weight:500;color:var(--ink);letter-spacing:1px;white-space:nowrap}
  .contact-bar{position:absolute;left:440px;top:570px;width:520px;height:38px;background:var(--blue);border-radius:19px 0 0 19px;display:flex;align-items:center;padding-left:20px;gap:24px;color:#fff;white-space:nowrap}
  .contact-bar__phone{font-size:20px;font-weight:500;display:flex;align-items:center;gap:4px;white-space:nowrap}
  .contact-bar__web{font-size:13px;display:flex;align-items:center;gap:8px;white-space:nowrap}
  .icon{width:20px;height:20px;flex:none}
  .offer{position:absolute;left:35px;color:#fff}
  .offer__title{font-size:22px;font-weight:400;letter-spacing:.3px;white-space:nowrap}
  .offer__text{width:405px;font-size:10.6px;line-height:1.25;margin-top:8px}
  .services{position:absolute;left:35px;top:442px;display:grid;grid-template-columns:86px 78px 126px 120px;row-gap:14px;color:#fff;list-style:none}
  .service{display:flex;gap:6px;font-size:9px;line-height:1.15;font-weight:500}
  .service__tick{width:11px;height:11px;border:1px solid var(--green);border-radius:50%;flex:none;margin-top:2px}
  .footer-bar{position:absolute;left:0;top:550px;width:505px;height:48px;background:var(--green);border-radius:0 24px 24px 0;display:flex;align-items:center;padding-left:33px;gap:20px;color:#fff;white-space:nowrap}
  .footer-bar__phone{font-size:18px;font-weight:500;display:flex;align-items:center;gap:4px;white-space:nowrap}
  .footer-bar__web{font-size:12px;display:flex;align-items:center;gap:7px;white-space:nowrap}
  .stamp{position:absolute;left:813px;top:62px;width:87px;height:87px;background:var(--stamp)}
  .address-line{position:absolute;left:590px;width:244px;height:1px;background:var(--rule)}
</style>
</head>
<body>
<main class="canvas">

  <!-- Front of postcard -->
  <section class="card card--front">
    <svg class="layer" viewBox="0 0 944 630" width="944" height="630">
      <defs>
        <linearGradient id="clinicTone" x1="0" y1="0" x2="1" y2="1">
          <stop offset="0" stop-color="#f4f5f7"/>
          <stop offset=".6" stop-color="#d7dbe2"/>
          <stop offset="1" stop-color="#b9c0cb"/>
        </linearGradient>
        <linearGradient id="toothTone" x1="0" y1="0" x2="0" y2="1">
          <stop offset="0" stop-color="#f7f7f7"/>
          <stop offset="1" stop-color="#cfd2d6"/>
        </linearGradient>
      </defs>
      <rect role="img" aria-label="Photo of a dentist examining a smiling patient in the dental chair" x="400" y="0" width="544" height="520" fill="url(#clinicTone)"/>
      <path d="M0,420 C40,360 90,330 150,345 C250,370 380,440 520,470 C650,500 720,460 800,400 C860,355 910,320 944,325 L944,630 L0,630 Z" fill="var(--blue)"/>
      <path d="M0,452 C60,392 130,386 220,410 C330,440 420,482 520,510 C640,542 760,470 860,402 C900,376 930,366 944,362 L944,630 L0,630 Z" fill="var(--green)"/>
      <rect role="img" aria-label="Illustration of a white tooth with a dental mirror" x="705" y="330" width="170" height="230" rx="40" fill="url(#toothTone)"/>
      <circle role="img" aria-label="Portrait photo of the dentist" cx="298" cy="475" r="76" fill="#d9dde3" stroke="#fff" stroke-width="5"/>
    </svg>

    <div class="brand" style="left:50px;top:25px">
      <span class="brand__dot"></span>
      <span class="brand__name">BROOKHOLLOW<br>FAMILY DENTISTRY</span>
    </div>

    <h1 class="headline">Your Top Rated</h1>
    <h2 class="subhead">Raleigh Dentist</h2>
    <p class="intro">Lorem Ipsum is simply dummy text of the printing and typesetting industry. Lorem Ipsum has been the industry's standard dummy text ever since the 1500s,</p>

    <p class="accepting">WE ARE<br>ACCEPTING<strong>NEW<br>PATIENTS</strong></p>
    <span class="accepting__rule"></span>

    <p class="contact-title">CONTACT US</p>
    <div class="contact-bar">
      <span class="contact-bar__phone">
        <svg class="icon" viewBox="0 0 24 24" fill="none" stroke="#fff" stroke-width="1.8"><path d="M5 3h4l2 5-2.5 1.5a11 11 0 0 0 6 6L16 13l5 2v4a2 2 0 0 1-2 2A17 17 0 0 1 3 5a2 2 0 0 1 2-2z"/></svg>
        919-555-0142
      </span>
      <span class="contact-bar__web">
        <svg class="icon" viewBox="0 0 24 24" fill="none" stroke="#fff" stroke-width="1.8"><circle cx="12" cy="12" r="9"/><path d="M3 12h18M12 3c3 3 3 15 0 18M12 3c-3 3-3 15 0 18"/></svg>
        brookhollowfamilydentistry.example
      </span>
    </div>
  </section>

  <!-- Back of postcard -->
  <section class="card card--back">
    <svg class="layer" viewBox="0 0 944 630" width="944" height="630">
      <defs>
        <linearGradient id="treatTone" x1="0" y1="0" x2="1" y2="1">
          <stop offset="0" stop-color="#d9e6f2"/>
          <stop offset="1" stop-color="#a9b6c6"/>
        </linearGradient>
        <linearGradient id="toothToneBack" x1="0" y1="0" x2="0" y2="1">
          <stop offset="0" stop-color="#f7f7f7"/>
          <stop offset="1" stop-color="#cfd2d6"/>
        </linearGradient>
      </defs>
      <rect role="img" aria-label="Photo of a dental hygienist treating a patient" x="0" y="0" width="320" height="200" fill="url(#treatTone)"/>
      <path d="M0,185 C60,170 110,175 170,190 C230,205 280,195 330,175 L420,200 C480,240 500,320 470,420 C450,480 430,560 425,630 L0,630 Z" fill="var(--blue)"/>
      <rect role="img" aria-label="Illustration of a white tooth with a dental mirror" x="330" y="40" width="150" height="235" rx="40" fill="url(#toothToneBack)"/>
    </svg>

    <div class="offer" style="top:250px">
      <h3 class="offer__title">WE OFFER</h3>
      <p class="offer__text">We are a family dental office that provides 99% of the dental service for the entire family, including IV sedation, wisdom teeth extraction, implant, Clearvanta, root canal, teeth whiting et cl. We currently have promotion for Clearvanta, implant and new patients who don't have insurance. 1500 off Clearvanta, 2000 off for implant, 98 dollars for new patient that cover exam, x-ray, and regular cleaning. We also offer financing option.</p>
    </div>
    <h3 class="offer offer__title" style="top:398px">OUR SERVICES</h3>
    <ul class="services">
      <li class="service"><span class="service__tick"></span>Short- Term<br>Braces</li>
      <li class="service"><span class="service__tick"></span>Cosmetic<br>Dentistry</li>
      <li class="service"><span class="service__tick"></span>Implant-Supported<br>Dentures</li>
      <li class="service"><span class="service__tick"></span>Implant-Supported<br>Dentures</li>
      <li class="service"><span class="service__tick"></span>Root Canal<br>Therapy</li>
      <li class="service"><span class="service__tick"></span>Teeth<br>Whitening</li>
      <li class="service"><span class="service__tick"></span>Porcelain Veneers</li>
      <li class="service"><span class="service__tick"></span>Dental Crowns</li>
    </ul>

    <div class="footer-bar">
      <span class="footer-bar__phone">
        <svg class="icon" viewBox="0 0 24 24" fill="none" stroke="#fff" stroke-width="1.8"><path d="M5 3h4l2 5-2.5 1.5a11 11 0 0 0 6 6L16 13l5 2v4a2 2 0 0 1-2 2A17 17 0 0 1 3 5a2 2 0 0 1 2-2z"/></svg>
        919-555-0142
      </span>
      <span class="footer-bar__web">
        <svg class="icon" viewBox="0 0 24 24" fill="none" stroke="#fff" stroke-width="1.8"><circle cx="12" cy="12" r="9"/><path d="M3 12h18M12 3c3 3 3 15 0 18M12 3c-3 3-3 15 0 18"/></svg>
        brookhollowfamilydentistry.example
      </span>
    </div>

    <div class="brand" style="left:565px;top:85px;gap:6px">
      <span class="brand__dot" style="width:44px;height:44px;border-width:2px"></span>
      <span class="brand__name" style="font-size:15px">BROOKHOLLOW<br>FAMILY DENTISTRY</span>
    </div>
    <span class="stamp"></span>
    <span class="address-line" style="top:285px"></span>
    <span class="address-line" style="top:335px"></span>
    <span class="address-line" style="top:382px"></span>
  </section>

</main>
</body>
</html>
```